Brisco Beverage Co.

Brisco is a new beverage company that currently specializes in energy and hydration. I need label design for the bottles. The label will be a full sleeve so free free to use the entire bottle. The premise behind the product is that its a Brisco from the competition. The label needs to say smart, strong, expensive. The background for the label will be black.
Updates

I need an entire label design as well as logo

Target Market(s)

20-30 year old active people.

Industry/Entity Type

It Company

Logo Text

By athletes for the athlete in all of us.

Logo styles of interest
Pictorial/Combination Logo
Wordmark Logo
Requirements
Must have
• the flavors are fruit based. Blackberry lime, mango pineapple, mango berry, strawberry kiwi. Incorporate natural looking fruit into the design.

```html
<!DOCTYPE html>
<html lang="en">
<head>
<meta charset="utf-8">
<title>Brisco – Blackberry &amp; Lime Sleeve Label</title>
<link rel="stylesheet" href="https://fonts.googleapis.com/css2?family=Anton&family=Oswald:wght@500&family=Open+Sans&family=Italianno&family=Tinos&display=swap">
<style>
  :root {
    --paper: #ffffff;
    --ink: #0b0b0b;
    --cap: #111111;
    --purple: #7a3f93;
    --purple-deep: #5a3190;
    --purple-neck: #6a35a0;
    --lime: #c8d52b;
    --sleeve-white: #f4f4f4;
    --sleeve-grey: #9a9a9a;
    --copy: #d8d8d8;
  }
  html, body {
    margin: 0;
    padding: 0;
    overflow: hidden;
    background: var(--paper);
  }
  .canvas {
    display: block;
    width: 983px;
    height: 1200px;
  }
  .brand-letter {
    font-family: "Oswald", sans-serif;
    font-weight: 500;
    font-size: 62px;
    text-anchor: middle;
  }
  .brand-letter--light { fill: var(--paper); }
  .brand-letter--dark { fill: var(--ink); }
  .volume-badge__text {
    font-family: "Anton", sans-serif;
    font-size: 25px;
    fill: var(--ink);
    text-anchor: middle;
  }
  .flavour-name {
    font-family: "Italianno", cursive;
    font-size: 44px;
    fill: var(--ink);
  }
  .label-copy {
    font-family: "Open Sans", sans-serif;
    font-size: 12.5px;
    fill: var(--copy);
  }
  .abv {
    font-family: "Tinos", serif;
    font-size: 11px;
    fill: var(--ink);
  }
</style>
</head>
<body>
<svg class="canvas" viewBox="0 0 983 1200" xmlns="http://www.w3.org/2000/svg">
  <defs>
    <clipPath id="bottle-shape">
      <path d="M405,62 L510,62 C514,150 520,220 540,280 C570,340 598,380 598,470 L598,1150 Q598,1162 586,1162 L342,1162 Q330,1162 330,1150 L330,470 C330,380 360,340 385,280 C400,220 402,150 405,62 Z"/>
    </clipPath>
    <linearGradient id="sleeve-stripe" x1="0" y1="0" x2="0" y2="1">
      <stop offset="0" stop-color="var(--sleeve-white)"/>
      <stop offset="0.6" stop-color="#e6e6e6"/>
      <stop offset="1" stop-color="var(--sleeve-grey)"/>
    </linearGradient>
    <linearGradient id="neck-fill" x1="0" y1="0" x2="0" y2="1">
      <stop offset="0" stop-color="#7a3aa6"/>
      <stop offset="1" stop-color="var(--purple-deep)"/>
    </linearGradient>
    <radialGradient id="fruit-tones" cx="0.4" cy="0.5" r="0.7">
      <stop offset="0" stop-color="#4b3fa0"/>
      <stop offset="0.55" stop-color="#231a4a"/>
      <stop offset="0.8" stop-color="#6e8f2a"/>
      <stop offset="1" stop-color="#b8d34a"/>
    </radialGradient>
    <radialGradient id="neck-berry-tones" cx="0.5" cy="0.5" r="0.5">
      <stop offset="0" stop-color="#7d4ab0"/>
      <stop offset="1" stop-color="#6a35a0" stop-opacity="0"/>
    </radialGradient>
  </defs>

  <!-- Left purple tag -->
  <g class="side-tag side-tag--purple">
    <rect x="164" y="513" width="96" height="612" fill="var(--purple)"/>
    <text class="brand-letter brand-letter--light">
      <tspan x="212" y="585">B</tspan>
      <tspan x="212" y="660">R</tspan>
      <tspan x="212" y="735">I</tspan>
      <tspan x="212" y="810">S</tspan>
      <tspan x="212" y="885">C</tspan>
      <tspan x="212" y="960">O</tspan>
    </text>
  </g>

  <!-- Right lime tag -->
  <g class="side-tag side-tag--lime">
    <rect x="690" y="508" width="96" height="614" fill="var(--lime)"/>
    <text class="brand-letter brand-letter--light">
      <tspan x="738" y="580">B</tspan>
      <tspan x="738" y="655">R</tspan>
      <tspan x="738" y="730">I</tspan>
      <tspan x="738" y="805">S</tspan>
      <tspan x="738" y="880">C</tspan>
      <tspan x="738" y="955">O</tspan>
    </text>
  </g>

  <!-- Bottle sleeve -->
  <g class="bottle">
    <rect class="bottle__cap" x="398" y="8" width="119" height="58" rx="8" fill="var(--cap)"/>
    <g clip-path="url(#bottle-shape)">
      <rect class="sleeve__neck" x="320" y="60" width="290" height="420" fill="url(#neck-fill)"/>
      <ellipse class="sleeve__neck-fruit" cx="445" cy="315" rx="52" ry="72" fill="url(#neck-berry-tones)" role="img" aria-label="Photograph of a blackberry fading into the purple neck"/>
      <rect class="sleeve__body" x="320" y="470" width="290" height="700" fill="var(--ink)"/>
      <rect class="sleeve__stripe" x="350" y="470" width="93" height="700" fill="url(#sleeve-stripe)"/>
      <rect class="sleeve__band" x="443" y="470" width="42" height="700" fill="var(--purple-deep)"/>

      <text class="brand-letter brand-letter--dark">
        <tspan x="396" y="580">B</tspan>
        <tspan x="396" y="655">R</tspan>
        <tspan x="396" y="730">I</tspan>
        <tspan x="396" y="805">S</tspan>
        <tspan x="396" y="880">C</tspan>
        <tspan x="396" y="955">O</tspan>
      </text>

      <text class="flavour-name" transform="translate(475 890) rotate(-90)">Blackberry &amp; lime</text>

      <text class="label-copy">
        <tspan x="491" y="640">Product of South</tspan>
        <tspan x="491" y="659">Africa</tspan>
        <tspan x="491" y="695">Accullor eptas-</tspan>
        <tspan x="491" y="714">perio. Mint alicien</tspan>
        <tspan x="491" y="733">volorer oviduntem</tspan>
        <tspan x="491" y="752">delluptatquo</tspan>
        <tspan x="491" y="771">bersped itaqui</tspan>
        <tspan x="491" y="790">ommolore rem</tspan>
      </text>

      <ellipse class="sleeve__fruit" cx="515" cy="1030" rx="100" ry="118" fill="url(#fruit-tones)" role="img" aria-label="Photograph of blackberries with a halved lime"/>

      <text class="abv" x="528" y="1128">40%VOL</text>
    </g>

    <g class="volume-badge">
      <circle cx="461" cy="423" r="42" fill="var(--lime)"/>
      <text class="volume-badge__text" x="461" y="436">70CL</text>
    </g>
  </g>
</svg>
</body>
</html>
```